Gently Windswept needs an eye catching marketing flyer

Our new Lumenvale Method(r) business needs an eye catching marketing flyer. We think A5 sizing?
website link (where you can understand more about breathwork is www.gentlywindswept-example.co.uk)
Design whatever you would like to design some things that could be of use to mention are below. Will leave it in your capable hands.
Logo files for Gently Windswept attached, use whichever one is best for your design, should be the main logo and colour scheme for the flyer, the second logo is that of Lumenvale Method(r) the breath school who's body of work we will be delivering. This can be anywhere on the flyer
Flyer is needed to get people interested in breathwork, the potential benefits for breathing better
We offer 1:1 sessions, workshops, corporate training
The flyer will have an offer code 'OpenDoor' which will give 15% off the bookers first 1:1 session
Flyer should include the following contact details: Maybe a "find out how breathwork can help you today. . . "
Carol Pennick (South): 07700 900 318
Rosalind Tarrow (Midlands): 07700 900 742
facebook: we.are.gentlywindswept
instagram: _gentlywindswept_

```html
<!DOCTYPE html>
<html lang="en">
<head>
<meta charset="utf-8">
<title>Gently Windswept – Breathing Better Flyer</title>
<link rel="stylesheet" href="https://fonts.googleapis.com/css2?family=Montserrat:wght@500;600;700;800;900&display=swap">
<style>
  :root {
    --page: #f0f0f0;
    --navy: #0b1c36;
    --navy-deep: #050a16;
    --cyan: #14c8dc;
    --cyan-dark: #0d8fa0;
    --purple: #8a1fe0;
    --magenta: #7b1a8f;
    --blue-line: #2357e8;
    --white: #ffffff;
    --ink: #111827;
  }
  * { box-sizing: border-box; margin: 0; padding: 0; }
  html, body {
    width: 783px; height: 1200px; overflow: hidden;
    background: var(--page);
    font-family: "Montserrat", Arial, sans-serif;
  }
  .flyer {
    position: absolute; left: 21px; top: 77px;
    width: 724px; height: 1022px;
    transform: scale(1.022); transform-origin: top left;
    overflow: hidden;
    background:
      radial-gradient(ellipse 420px 200px at 610px 860px, rgba(150,30,170,.55), transparent 70%),
      radial-gradient(ellipse 380px 220px at 200px 800px, rgba(40,80,190,.45), transparent 70%),
      linear-gradient(180deg, #0d2240 0%, var(--navy) 35%, var(--navy-deep) 60%, #120a2a 100%);
    box-shadow: 0 4px 14px rgba(0,0,0,.25);
    color: var(--white);
  }
  .brand {
    position: absolute; left: 72px; top: 40px; width: 170px; height: 170px;
  }
  .brand-glow {
    position: absolute; inset: 0 0 60px 20px;
    border-radius: 50%;
    background: radial-gradient(ellipse at 60% 45%, rgba(60,140,230,.45), rgba(120,60,220,.15) 55%, transparent 75%);
  }
  .brand-ring {
    position: absolute; left: 16px; top: 48px; width: 118px; height: 118px;
    border: 1.5px solid rgba(60,120,230,.8); border-radius: 50%;
  }
  .brand-name {
    position: absolute; left: 0; top: 88px; width: 160px;
    text-align: center; font-weight: 600; font-size: 19px; line-height: 1.15;
    color: var(--white);
  }
  .headline { position: absolute; left: 42px; top: 218px; font-weight: 900; letter-spacing: -1.5px; line-height: 1; }
  .headline .line-1 { display: block; font-size: 47px; color: var(--white); }
  .headline .line-2 { display: block; font-size: 50px; color: var(--cyan); margin-top: 6px; }
  .headline .line-3 { display: block; font-size: 88px; color: var(--cyan); margin-top: 2px; letter-spacing: -3px; }
  .hero-photo {
    position: absolute; left: 370px; top: 45px; width: 354px; height: 410px;
    background:
      radial-gradient(ellipse 110px 150px at 200px 190px, rgba(235,235,240,.55), transparent 75%),
      radial-gradient(ellipse 170px 60px at 190px 380px, rgba(110,120,140,.6), transparent 80%),
      radial-gradient(ellipse 190px 160px at 130px 120px, rgba(40,170,220,.35), transparent 70%),
      radial-gradient(ellipse 170px 170px at 200px 230px, rgba(200,120,120,.25), transparent 75%);
  }
  .offer-rule { position: absolute; left: 0; right: 0; top: 472px; height: 2px; background: var(--blue-line); }
  .offer-tab {
    position: absolute; left: 212px; top: 453px; width: 300px; height: 40px;
    background: var(--purple); border-radius: 0 0 30px 30px;
    text-align: center; font-weight: 800; font-size: 27px; line-height: 40px; letter-spacing: .5px;
  }
  .services { position: absolute; left: 0; right: 0; top: 515px; height: 130px; }
  .service { position: absolute; top: 0; text-align: center; font-weight: 700; font-size: 17px; letter-spacing: .3px; }
  .service .badge {
    width: 82px; height: 82px; margin: 0 auto 16px; border-radius: 50%;
    border: 2px dotted var(--white); padding: 5px;
  }
  .service .badge-inner {
    width: 100%; height: 100%; border-radius: 50%; background: var(--cyan);
    display: flex; align-items: center; justify-content: center;
  }
  .service .badge-core {
    width: 48px; height: 48px; border-radius: 50%; background: var(--white);
    display: flex; align-items: center; justify-content: center;
  }
  .service-one { left: 55px; width: 140px; }
  .service-two { left: 240px; width: 150px; }
  .service-three { left: 425px; width: 240px; }
  .divider { position: absolute; top: 515px; width: 1px; height: 125px; background: rgba(255,255,255,.35); }
  .coupon {
    position: absolute; left: 138px; top: 666px; width: 448px; height: 90px;
    display: flex; border-radius: 10px; overflow: hidden;
    box-shadow: 0 12px 14px -8px rgba(0,0,0,.7);
  }
  .coupon-code { width: 277px; background: var(--cyan); padding: 8px 0 8px 12px; }
  .coupon-code span {
    display: block; height: 100%; border: 1.5px dashed var(--cyan-dark); border-right: none;
    border-radius: 6px 0 0 6px; font-weight: 800; font-size: 30px; letter-spacing: 1px;
    color: #0b3a48; line-height: 70px; text-align: center;
  }
  .coupon-terms {
    flex: 1; background: var(--white); color: var(--ink); padding: 10px 12px 0 16px;
    border-left: 2px dashed #1a2a3a;
  }
  .coupon-terms .lead { font-weight: 700; font-size: 13px; letter-spacing: .3px; }
  .coupon-terms .deal { display: flex; align-items: center; gap: 4px; margin-top: 1px; border-bottom: 1px solid #333; padding-bottom: 2px; }
  .coupon-terms .pct { font-weight: 800; font-size: 38px; color: var(--purple); line-height: 1; }
  .coupon-terms .off { font-weight: 800; font-size: 13px; line-height: .9; }
  .coupon-terms .off small { display: block; font-size: 7px; font-weight: 700; }
  .coupon-terms .session { font-weight: 700; font-size: 9px; text-align: center; margin-top: 4px; }
  .cta { position: absolute; left: 0; right: 0; top: 794px; text-align: center; font-weight: 700; font-size: 18px; letter-spacing: .6px; }
  .contacts { position: absolute; left: 0; right: 0; top: 840px; }
  .contact { position: absolute; top: 0; display: flex; gap: 12px; font-weight: 700; font-size: 13px; line-height: 1.5; }
  .contact .thumb {
    width: 64px; height: 68px; border: 1px solid rgba(255,255,255,.8);
    background: radial-gradient(ellipse at 40% 35%, rgba(60,140,230,.45), transparent 70%), var(--navy-deep);
  }
  .contact .thumb.partner { background: radial-gradient(circle, #b86ad0 0%, #5a2a80 55%, #2a1240 100%); }
  .contact .phone { color: var(--cyan); letter-spacing: .5px; }
  .contact-south { left: 53px; }
  .contact-midlands { left: 261px; }
  .contact-partner { left: 472px; }
  .footer-rule { position: absolute; left: 0; right: 0; top: 943px; height: 6px; background: var(--cyan); }
  .footer {
    position: absolute; left: 0; right: 0; top: 949px; bottom: 0; background: var(--white);
    display: flex; align-items: center; justify-content: center; gap: 14px;
    color: var(--ink); font-weight: 700; font-size: 20px;
  }
  .footer .handle { display: flex; align-items: center; gap: 10px; }
  .footer .mark { width: 20px; height: 20px; border-radius: 4px; background: #1877f2; }
  .footer .mark.round { border-radius: 50%; background: #e4405f; }
  .footer .sep { width: 1.5px; height: 28px; background: var(--ink); }
</style>
</head>
<body>
  <main class="flyer">
    <div class="brand">
      <div class="brand-glow" role="img" aria-label="Soft blue feather flourish behind the brand name"></div>
      <div class="brand-ring"></div>
      <div class="brand-name">Gently<br>Windswept</div>
    </div>

    <div class="hero-photo" role="img" aria-label="Woman in a white t-shirt meditating cross-legged, with a glowing blue feather and a gold mandala behind her"></div>

    <h1 class="headline">
      <span class="line-1">BENEFITS FOR</span>
      <span class="line-2">BREATHING</span>
      <span class="line-3">BETTER</span>
    </h1>

    <div class="offer-rule"></div>
    <div class="offer-tab">WE OFFER</div>

    <section class="services">
      <div class="service service-one">
        <div class="badge"><div class="badge-inner"><div class="badge-core">
          <svg width="30" height="30" viewBox="0 0 30 30" fill="none" stroke="#1a1a1a" stroke-width="1.4">
            <rect x="7" y="3" width="16" height="10" rx="1"/><circle cx="11" cy="8" r="2"/><circle cx="19" cy="8" r="2"/>
            <circle cx="8" cy="19" r="2.5"/><circle cx="15" cy="19" r="2.5"/><circle cx="22" cy="19" r="2.5"/>
            <path d="M4 27c0-3 8-3 8 0M11 27c0-3 8-3 8 0M18 27c0-3 8-3 8 0"/>
          </svg>
        </div></div></div>
        1:1 SESSIONS
      </div>
      <div class="service service-two">
        <div class="badge"><div class="badge-inner"><div class="badge-core">
          <svg width="30" height="30" viewBox="0 0 30 30" fill="none" stroke="#1a1a1a" stroke-width="1.4">
            <rect x="4" y="3" width="22" height="12" rx="1"/><circle cx="11" cy="9" r="2"/><path d="M16 7h7M16 10h5"/>
            <circle cx="8" cy="21" r="2"/><circle cx="15" cy="21" r="2"/><circle cx="22" cy="21" r="2"/>
            <path d="M5 27c0-2 6-2 6 0M12 27c0-2 6-2 6 0M19 27c0-2 6-2 6 0"/>
          </svg>
        </div></div></div>
        WORKSHOPS
      </div>
      <div class="service service-three">
        <div class="badge"><div class="badge-inner"><div class="badge-core">
          <svg width="30" height="30" viewBox="0 0 30 30" fill="none" stroke="#1a1a1a" stroke-width="1.4">
            <rect x="12" y="4" width="14" height="10" rx="1"/><path d="M15 11l3-3 3 2 3-3"/>
            <circle cx="9" cy="12" r="2.5"/><path d="M4 24c0-5 10-5 10 0"/>
            <rect x="4" y="20" width="14" height="7" rx="1"/>
          </svg>
        </div></div></div>
        CORPORATE TRAINING
      </div>
    </section>
    <div class="divider" style="left:215px"></div>
    <div class="divider" style="left:405px"></div>

    <section class="coupon">
      <div class="coupon-code"><span>OPENDOOR</span></div>
      <div class="coupon-terms">
        <div class="lead">WHICH WILL GIVE</div>
        <div class="deal"><span class="pct">15%</span><span class="off">OFF<small>THE BOOKERS</small></span></div>
        <div class="session">FIRST 1:1 SESSION</div>
      </div>
    </section>

    <p class="cta">FIND OUT HOW BREATHWORK CAN HELP YOU TODAY</p>

    <section class="contacts">
      <div class="contact contact-south">
        <div class="thumb"></div>
        <div>Carol Pennick<br>(South)<br><span class="phone">07700 900 318</span></div>
      </div>
      <div class="contact contact-midlands">
        <div class="thumb"></div>
        <div>Rosalind<br>Tarrow (Midlands)<br><span class="phone">07700 900 742</span></div>
      </div>
      <div class="contact contact-partner">
        <div class="thumb partner"></div>
        <div>Lumenvale<br>Method®</div>
      </div>
    </section>

    <div class="footer-rule"></div>
    <footer class="footer">
      <span class="handle"><span class="mark"></span>we.are.gentlywindswept</span>
      <span class="sep"></span>
      <span class="handle"><span class="mark round"></span>_gentlywindswept_</span>
    </footer>
  </main>
</body>
</html>
```